Subscription box needs a bold design for our lock front mailer box

We are a new subscription box service called Petal Crest Box filled with an array of delightful products made by women artisans and business owners. Products include handcrafted bath, beauty and spa products, gourmet delights, home and lifestyle goods, jewelry and accessories. We also place great importance on obtaining organic products from sustainable sources where possible.
Our focus is on lifting women up and on inspiring our customers to do so too. We do this by sourcing all of our products from women, creating a monthly “Kind Turn” card for each box with ideas on how to give another woman a boost, and donating 10% of our proceeds to a woman-focused charity each month. We believe that we will all be stronger if we work together.
We need a bold design for our mailing box that incorporates our logo, our website address, our tag line and possibly our mascot.
The box will be white with red print. We have a template for PDF and EPS from the company we will use to produce the boxes. We are attaching templates, logo, mascot photo, sample pattern and ideas. We would like a designer that can bring their own ideas and we are very open to new thoughts.

Target Market(s)

Women, 25 to 65. Educated with significant disposable income.

Industry/Entity Type

Business

Colors
ec1f27

Requirements
Must have
• A bold look. Must include our logo and tag line "Uplift Yourself, Kind Turn Women"
• Will be red print on a white box.
Nice to have
• Have included file with ideas but am very open to other thoughts and designs.

```html
<!DOCTYPE html>
<html lang="en">
<head>
<meta charset="utf-8">
<title>Petal Crest Box – Mailer Dieline</title>
<link href="https://fonts.googleapis.com/css2?family=Roboto:wght@400;700&display=swap" rel="stylesheet">
<style>
  :root {
    --brand-red: #e31e26;
    --pattern-red: #e7373d;
    --cut-line: #4a4a4a;
    --fold-line: #e31e26;
    --paper: #ffffff;
  }
  html, body {
    margin: 0;
    padding: 0;
    width: 1200px;
    height: 1112px;
    overflow: hidden;
    background: var(--paper);
  }
  .dieline {
    display: block;
    width: 1200px;
    height: 1112px;
    font-family: "Roboto", Arial, sans-serif;
  }
  .cut { fill: var(--paper); stroke: var(--cut-line); stroke-width: 1; }
  .fold { stroke: var(--fold-line); stroke-width: 0.8; stroke-dasharray: 3 3; fill: none; }
  .band { fill: var(--brand-red); }
  .pattern-field { fill: var(--pattern-red); }
  .window { fill: var(--paper); }
  .mascot-area { fill: var(--brand-red); opacity: 0.85; }
  .lock-slot { fill: none; stroke: var(--cut-line); stroke-width: 0.8; }
  .web-address { fill: var(--paper); font-size: 15px; font-weight: 400; }
  .social-line { fill: var(--brand-red); font-size: 16px; font-weight: 400; }
  .social-mark { fill: var(--brand-red); }
  .logo-name { fill: var(--brand-red); font-size: 40px; font-weight: 700; letter-spacing: 0.5px; }
  .tagline { fill: var(--brand-red); font-size: 21px; font-weight: 400; }
</style>
</head>
<body>
<svg class="dieline" viewBox="0 0 1200 1112" xmlns="http://www.w3.org/2000/svg">

  <!-- Lid top flap -->
  <rect class="cut" x="285" y="46" width="629" height="168"/>
  <!-- Lid side flaps -->
  <path class="cut" d="M226,219 L38,219 L38,304 L31,307 L31,375 L38,378 L38,464 L226,464 Z"/>
  <path class="cut" d="M974,219 L1162,219 L1162,304 L1169,307 L1169,375 L1162,378 L1162,464 L974,464 Z"/>
  <!-- Back panel -->
  <rect class="cut" x="285" y="470" width="629" height="168"/>

  <!-- Red side bands -->
  <path class="band" d="M210,219 L226,214 L400,214 L400,470 L226,470 L210,464 Z"/>
  <path class="band" d="M798,214 L974,214 L990,219 L990,464 L974,470 L798,470 Z"/>
  <text class="web-address" transform="translate(312,342) rotate(-90)" text-anchor="middle">www.PetalCrestBox.com</text>
  <text class="web-address" transform="translate(882,342) rotate(90)" text-anchor="middle">www.PetalCrestBox.com</text>

  <!-- Lid panel pattern with window -->
  <rect class="pattern-field" x="400" y="216" width="398" height="252" role="img" aria-label="Red and white interlocking ring pattern"/>
  <rect class="window" x="440" y="250" width="318" height="184" rx="16"/>
  <rect class="lock-slot" x="400" y="304" width="18" height="72"/>
  <rect class="lock-slot" x="780" y="304" width="18" height="72"/>

  <!-- Mascot and social line on top flap -->
  <rect class="mascot-area" x="494" y="82" width="70" height="98" rx="30" role="img" aria-label="Red line illustration of the pug mascot wearing a bead necklace"/>
  <text class="social-line" x="588" y="129">Come Be Social!</text>
  <text class="social-line" x="588" y="152">Visit us on Chirpbook</text>
  <rect class="social-mark" x="752" y="139" width="14" height="14"/>

  <!-- Front ear flaps -->
  <path class="cut" d="M418,645 L300,645 Q248,645 248,705 L248,780 Q248,832 300,858 L418,894 Z"/>
  <path class="cut" d="M781,645 L899,645 Q952,645 952,705 L952,780 Q952,832 899,858 L781,894 Z"/>

  <!-- Front panel -->
  <rect class="pattern-field" x="418" y="640" width="363" height="254" role="img" aria-label="Red and white interlocking ring pattern"/>
  <rect class="window" x="456" y="698" width="286" height="138" rx="14"/>
  <text class="logo-name" x="599" y="781" text-anchor="middle">PETAL CREST</text>

  <!-- Bottom tuck flap -->
  <path class="cut" d="M418,898 L296,908 Q284,909 286,920 Q300,1010 405,1066 L795,1066 Q900,1010 914,920 Q916,909 904,908 L781,898 Z"/>
  <text class="tagline" x="600" y="990" text-anchor="middle">Uplift Yourself, Kind Turn Women</text>

  <!-- Fold lines -->
  <line class="fold" x1="410" y1="46" x2="410" y2="214"/>
  <line class="fold" x1="790" y1="46" x2="790" y2="214"/>
  <line class="fold" x1="410" y1="470" x2="410" y2="638"/>
  <line class="fold" x1="790" y1="470" x2="790" y2="638"/>
  <line class="fold" x1="210" y1="219" x2="210" y2="464"/>
  <line class="fold" x1="990" y1="219" x2="990" y2="464"/>
  <line class="fold" x1="405" y1="900" x2="405" y2="1066"/>
  <line class="fold" x1="795" y1="900" x2="795" y2="1066"/>
</svg>
</body>
</html>
```